Packaging Design for Peach Halves in Syrup

Hello Designer,
We have to create a packaging design for a peach halves in syrup product.
The design should be eye-catching, appealing to the target europeen market, and convey the product's quality and freshness.
Peach halves in syrup, packed in glass jars with yellow lids. The jar size is as a picture attached below.
Logo : KORAM
Label Design: Design a label that prominently features the product name in english and french, "Peach Halves in Syrup," "Pêches en moitiés" and highlights key selling points such as "100% Natural" or "No Added Preservatives."
Visual Elements: Incorporate image or illustration of ripe peaches to emphasize the product's freshness and natural ingredients.
Color Scheme: Use a color scheme that complements the yellow lids, making the product stand out on the shelf. Consider using warm, inviting colors to evoke the feeling of freshness.

Nutritional Information: Include a panel for nutritional information.
ingredients list -Eng : peaches, water, Sugar.
-Fr : pêches, eau, sucre.
Barcode: leave a space for barcode.

Target Market(s)

Europe

Font styles to use
Serif
Decorative
Script

Requirements
Must have
• -Product name : ENG and FR, barcode, nutritional information, ingredients : Eng and French.

```html
<!DOCTYPE html>
<html lang="en">
<head>
<meta charset="utf-8">
<title>KORAM – Peach Halves in Syrup label</title>
<link href="https://fonts.googleapis.com/css2?family=Poppins:wght@400;600;800&family=Arimo:wght@400;700&display=swap" rel="stylesheet">
<style>
  :root{
    --page:#ffffff;
    --orange:#ff820c;
    --orange-light:#ffb453;
    --ribbon:#f0651f;
    --ribbon-dark:#d9531a;
    --navy:#2f3472;
    --white:#ffffff;
    --ink:#111111;
    --peach-a:#ffc25a;
    --peach-b:#f2622a;
  }
  html,body{margin:0;padding:0;overflow:hidden}
  body{width:1064px;height:1200px;background:var(--page);position:relative;font-family:"Poppins",sans-serif}
  .label{
    position:absolute;left:32px;top:356px;width:1000px;height:488px;
    background:radial-gradient(ellipse at 48% 50%,var(--orange-light) 0%,var(--orange) 62%);
    overflow:hidden;
  }
  /* nutrition panel */
  .nutrition{
    position:absolute;left:26px;top:63px;width:185px;height:351px;
    background:var(--white);padding:2px 6px;font-family:"Arimo",sans-serif;color:var(--ink);
  }
  .nutrition h2{margin:0;font-size:24px;font-weight:700;line-height:28px;letter-spacing:-.2px}
  .nutrition .row{display:flex;justify-content:space-between;font-size:9.5px;line-height:14.5px;border-top:1px solid #777}
  .nutrition .row.indent{padding-left:10px}
  .nutrition .row.indent2{padding-left:21px}
  .nutrition .serving{border-top:1px solid var(--ink);font-weight:700;font-size:11px;line-height:15px}
  .nutrition .thick{border-top:6px solid var(--ink)}
  .nutrition .amount{font-size:8px;font-weight:700;line-height:10px;margin-top:3px}
  .nutrition .calories{display:flex;justify-content:space-between;align-items:flex-end;font-weight:700;font-size:17px;line-height:22px}
  .nutrition .calories span:last-child{font-size:25px}
  .nutrition .mid{border-top:3px solid var(--ink)}
  .nutrition .dv{text-align:right;font-size:8.5px;font-weight:700;line-height:12px}
  .nutrition b{font-weight:700}
  .nutrition .note{border-top:3px solid var(--ink);font-size:6px;line-height:7.5px;padding-top:2px}
  /* brand */
  .brand{position:absolute;left:0;width:100%;top:52px;display:flex;justify-content:center;align-items:center;gap:10px}
  .brand .mark{width:22px;height:22px;background:var(--navy)}
  .brand .name{font-size:54px;font-weight:800;color:var(--navy);line-height:1;letter-spacing:1px}
  .illustration{
    position:absolute;left:353px;top:156px;width:291px;height:194px;border-radius:46% 46% 40% 40%;
    background:radial-gradient(ellipse at 35% 45%,var(--peach-a) 0%,var(--peach-b) 80%,transparent 81%);
  }
  .ribbon{position:absolute;left:278px;top:352px;width:442px;height:86px}
  .ribbon svg{position:absolute;inset:0}
  .ribbon .title{position:absolute;left:0;right:0;top:8px;text-align:center;color:var(--white);font-weight:800;font-size:31px;line-height:38px}
  .ribbon .subtitle{position:absolute;left:0;right:0;top:46px;text-align:center;color:var(--white);font-weight:400;font-size:25px;line-height:30px}
  .claims{position:absolute;top:447px;left:298px;display:flex;gap:24px;color:var(--white);font-weight:600;font-size:17px;line-height:24px}
  .claims span{display:flex;align-items:center;gap:4px}
  /* info column */
  .info{position:absolute;left:792px;top:173px;width:190px;font-family:"Arimo",sans-serif;color:var(--ink);font-size:13px;line-height:15px}
  .info .maker{text-align:center;margin-top:18px;width:180px}
  .barcode-space{position:absolute;left:798px;top:310px;width:170px;height:87px;background:var(--white);display:flex;align-items:center;justify-content:center;font-family:"Arimo",sans-serif;font-size:20px;color:var(--ink)}
  .disposal{position:absolute;left:836px;top:412px;display:flex;gap:16px}
</style>
</head>
<body>
  <section class="label">
    <div class="nutrition">
      <h2>Nutrition Facts</h2>
      <div class="row serving"><span>Serving size</span><span>1 Empanada</span></div>
      <div class="thick"></div>
      <div class="amount">Amount per serving</div>
      <div class="calories"><span>Calories</span><span>234</span></div>
      <div class="mid"></div>
      <div class="dv">% Daily Value*</div>
      <div class="row"><span><b>Total Fat</b> 10.5g</span><b>4.7%</b></div>
      <div class="row indent"><span>Saturated Fat 0.7g</span><b>0.3%</b></div>
      <div class="row indent"><span>Trans Fat 0g</span><b>0%</b></div>
      <div class="row"><span><b>Cholesterol</b> 0g</span><b>0%</b></div>
      <div class="row"><span><b>Sodium</b> 6.31mg</span><b></b></div>
      <div class="row"><span><b>Total Carbohydrate</b> 31.9g</span><b>6.3%</b></div>
      <div class="row indent"><span>Dietary Fiber 2.2g</span><b>0.44%</b></div>
      <div class="row indent"><span>Total Sugars 7.7g</span><b>1.5%</b></div>
      <div class="row indent2"><span>Added Sugars 1.1g</span><b>0.2%</b></div>
      <div class="row"><span><b>Protein</b> 3g</span><b>0.6%</b></div>
      <div class="thick"></div>
      <div class="row" style="border-top:0"><span>Vitamin D</span></div>
      <div class="row"><span>Calcium 0.92</span></div>
      <div class="row"><span>Iron 1.4</span></div>
      <div class="row"><span>Potassium 95.6mg</span></div>
      <div class="note">*The % Daily Value tells you how much a nutrient in a serving of food contributes to a daily diet. 2,000 calories a day is used for general nutrition advice.</div>
    </div>

    <div class="brand"><span class="mark"></span><span class="name">KORAM</span></div>

    <div class="illustration" role="img" aria-label="Illustration of a whole ripe peach and a peach half with its stone, with green leaves"></div>

    <div class="ribbon">
      <svg viewBox="0 0 442 86" width="442" height="86" aria-hidden="true">
        <polygon points="0,0 442,0 418,43 442,86 0,86 24,43" fill="var(--ribbon)"/>
        <polygon points="0,0 30,0 30,86 0,86 24,43" fill="var(--ribbon-dark)"/>
        <polygon points="442,0 412,0 412,86 442,86 418,43" fill="var(--ribbon-dark)"/>
      </svg>
      <div class="title">Peach Halves in Syrup</div>
      <div class="subtitle">Pêches en moitiés</div>
    </div>

    <div class="claims">
      <span><svg width="16" height="18" viewBox="0 0 16 18" aria-hidden="true"><path d="M2 2 C12 2 15 8 13 16 C6 15 2 10 2 2Z" fill="var(--white)"/></svg>100% Natural</span>
      <span><svg width="14" height="20" viewBox="0 0 14 20" aria-hidden="true"><path d="M7 1 C9 6 13 10 13 14 A6 6 0 0 1 1 14 C1 10 5 6 7 1Z" fill="none" stroke="var(--white)" stroke-width="1.5"/><circle cx="7" cy="14" r="2" fill="var(--white)"/></svg>No Added Preservatives</span>
    </div>

    <div class="info">
      <div><b>Eng :</b> peaches, water, Sugar.</div>
      <div><b>Fr :</b> pêches, eau, sucre.</div>
      <div class="maker">
        <div>Manufactured by</div>
        <div><b>KORAM</b></div>
        <div>???????????</div>
        <div>???????</div>
        <div>www.<b>koram</b>.com</div>
      </div>
    </div>

    <div class="barcode-space">BAR CODE</div>

    <div class="disposal">
      <svg width="42" height="38" viewBox="0 0 42 38" aria-hidden="true">
        <g fill="none" stroke="var(--ink)" stroke-width="6" stroke-linejoin="round">
          <path d="M21 5 L9 26 M33 26 L21 5 M9 32 L33 32"/>
        </g>
      </svg>
      <svg width="34" height="44" viewBox="0 0 34 44" aria-hidden="true">
        <circle cx="24" cy="5" r="4" fill="var(--ink)"/>
        <path d="M20 11 L28 11 L28 28 L31 43 L26 43 L24 30 L22 43 L18 43 L20 24 L14 20 L16 17 L20 20Z" fill="var(--ink)"/>
        <path d="M2 24 L16 24 L14 42 L4 42Z" fill="none" stroke="var(--ink)" stroke-width="2"/>
        <path d="M6 27 L7 40 M9 27 L9 40 M12 27 L11 40" stroke="var(--ink)" stroke-width="1.2"/>
      </svg>
    </div>
  </section>
</body>
</html>
```